Veltrix App's Dashboard Redesign

We are redesigning our existing Veltrix app (http://www.lunatrak.com) to use Veltrix's new Facet Design guidelines (read more here: http://www.plexora.com/design/).

We would like to see new designs of the app's main screen (see lunatrak_dashboard.png) from you.

The new dashboard screen design should:
A. follow Veltrix's new Facet Design guidelines
B. contain an actionbar at the top (with an icon for hints and a "hamburger menu icon" on the left)
C. contain 4 buttons to the app's other screens: 1. Edit today's symptoms, 2. Calendar view, 3. Timeline view, 4. Chart view. (Please, do not put the buttons into tabs, as we want to avoid putting tabs on other screens too)
D. keep the basic concept of the cycle wheel (circle/donut representing the days of cycle; distinguish passed/upcoming days of cycle; show current cycle day; show menses days/fertile days/ovulation day)
E. contain iconic or textual predictions of the number of days to the next menses/ovulation
F. be easily themable to different colors (as the app supports more color themes)

To get a better idea about the app in general and the dashboard/cycle wheel in particular, please install the app and read Petal Orbit Notes. This will help you understand the functional requirements.

Wheel

```html
<!DOCTYPE html>
<html lang="en">
<head>
<meta charset="utf-8">
<title>LunaTrak Dashboard Concepts</title>
<link rel="stylesheet" href="https://fonts.googleapis.com/css2?family=Roboto:wght@400;500&display=swap">
<style>
  :root {
    --canvas: #cfcfcf;
    --status: #c2185b;
    --toolbar: #ec407a;
    --surface: #fafafa;
    --sheet: #ffffff;
    --ink: #333333;
    --ink-soft: #8a8a8a;
    --accent: #7c4dff;
    --accent-light: #b388ff;
    --ring: #ff86ad;
    --menses: #ec407a;
    --divider: #e2e2e2;
    --nav: #000000;
  }
  * { box-sizing: border-box; margin: 0; padding: 0; }
  html, body { width: 694px; height: 1200px; overflow: hidden; background: var(--canvas); }
  body { font-family: "Roboto", sans-serif; }
  .board { position: relative; width: 756px; height: 1307px; transform: scale(0.918); transform-origin: 0 0; }
  .screen { position: absolute; width: 360px; height: 640px; background: var(--surface); overflow: hidden; }
  .screen--top-left { left: 10px; top: 8px; }
  .screen--top-right { left: 386px; top: 8px; }
  .screen--bottom-left { left: 10px; top: 659px; }
  .screen--bottom-right { left: 386px; top: 659px; }

  .status-bar { position: absolute; left: 0; top: 0; width: 360px; height: 24px; background: var(--status); }
  .status-bar__icons { position: absolute; right: 42px; top: 5px; }
  .status-bar__time { position: absolute; right: 8px; top: 5px; color: #fff; font-size: 13px; }

  .toolbar { position: absolute; left: 0; top: 24px; width: 360px; height: 56px; background: var(--toolbar); box-shadow: 0 2px 4px rgba(0,0,0,.18); z-index: 2; }
  .toolbar__title { position: absolute; left: 71px; top: 15px; color: #fff; font-size: 20px; font-weight: 500; }
  .toolbar .icon { position: absolute; top: 16px; width: 24px; height: 24px; fill: #fff; }

  .wheel { position: absolute; left: 0; width: 360px; height: 440px; }
  .wheel--a { top: 80px; }
  .wheel--b { top: 74px; }
  .wheel--c { top: 68px; }
  .wheel--d { top: 63px; }

  .fab { position: absolute; left: 288px; width: 56px; height: 56px; border-radius: 50%; background: var(--menses); box-shadow: 0 3px 6px rgba(0,0,0,.25); z-index: 3; }
  .fab .icon { position: absolute; left: 16px; top: 16px; width: 24px; height: 24px; fill: #fff; }

  .nav-bar { position: absolute; left: 0; bottom: 0; width: 360px; height: 48px; background: var(--nav); }

  .action-bar { position: absolute; left: 0; top: 544px; width: 360px; height: 48px; background: var(--sheet); border-top: 1px solid var(--divider); display: flex; }
  .action-bar__item { flex: 1; display: flex; align-items: center; justify-content: center; gap: 10px; font-size: 14px; font-weight: 500; color: var(--ink); border-left: 2px solid var(--divider); margin: 4px 0; }
  .action-bar__item:first-child { border-left: 0; }
  .action-bar__item .icon { width: 22px; height: 22px; fill: var(--accent); }

  .mode-sheet { position: absolute; left: 0; top: 496px; width: 360px; height: 96px; background: var(--sheet); border-top: 1px solid var(--divider); }
  .mode-sheet__title { position: absolute; left: 16px; top: 11px; font-size: 16px; color: var(--ink); }
  .mode-sheet__items { position: absolute; left: 0; top: 40px; width: 360px; display: flex; }
  .mode-sheet__item { flex: 1; text-align: center; font-size: 12px; color: var(--ink-soft); }
  .mode-sheet__item .icon { display: block; margin: 0 auto 4px; width: 22px; height: 22px; fill: var(--accent); }

  .mode-list { position: absolute; left: 0; top: 471px; width: 360px; height: 121px; background: var(--sheet); border-top: 1px solid var(--divider); list-style: none; padding-top: 8px; }
  .mode-list__item { height: 36px; display: flex; align-items: center; font-size: 14px; color: var(--ink); }
  .mode-list__item .icon { width: 22px; height: 22px; fill: var(--accent); margin: 0 42px 0 17px; }
</style>
</head>
<body>
<svg width="0" height="0" style="position:absolute">
  <defs>
    <symbol id="i-menu" viewBox="0 0 24 24"><path d="M3 18h18v-2H3v2zm0-5h18v-2H3v2zm0-7v2h18V6H3z"/></symbol>
    <symbol id="i-list" viewBox="0 0 24 24"><path d="M3 13h2v-2H3v2zm0 4h2v-2H3v2zm0-8h2V7H3v2zm4 4h14v-2H7v2zm0 4h14v-2H7v2zM7 7v2h14V7H7z"/></symbol>
    <symbol id="i-calendar" viewBox="0 0 24 24"><path d="M19 3h-1V1h-2v2H8V1H6v2H5c-1.11 0-1.99.9-1.99 2L3 19c0 1.1.89 2 2 2h14c1.1 0 2-.9 2-2V5c0-1.1-.9-2-2-2zm0 16H5V8h14v11zM7 10h5v5H7z"/></symbol>
    <symbol id="i-chart" viewBox="0 0 24 24"><path d="M3.5 18.49l6-6.01 4 4L22 6.92l-1.41-1.41-7.09 7.97-4-4L2 16.99z"/></symbol>
    <symbol id="i-hint" viewBox="0 0 24 24"><path d="M12 6a5 5 0 0 0-3 9v2h6v-2a5 5 0 0 0-3-9zM9 18h6v1.5a1.5 1.5 0 0 1-1.5 1.5h-3A1.5 1.5 0 0 1 9 19.5z"/><path d="M11 1h2v3h-2zM3 10h3v2H3zM18 10h3v2h-3zM4.2 4.6l1.4-1.4 2 2-1.4 1.4zM16.4 5.2l2-2 1.4 1.4-2 2z"/></symbol>
    <symbol id="i-edit" viewBox="0 0 24 24"><path d="M3 17.25V21h3.75L17.81 9.94l-3.75-3.75L3 17.25zM20.71 7.04c.39-.39.39-1.02 0-1.41l-2.34-2.34c-.39-.39-1.02-.39-1.41 0l-1.83 1.83 3.75 3.75 1.83-1.83z"/></symbol>
    <symbol id="i-check" viewBox="0 0 24 24"><path d="M9 16.17L4.83 12l-1.42 1.41L9 19 21 7l-1.41-1.41z"/></symbol>
    <symbol id="i-drop" viewBox="0 0 24 24"><path d="M12 2c-5.33 4.55-8 8.48-8 11.8 0 4.98 3.8 8.2 8 8.2s8-3.22 8-8.2c0-3.32-2.67-7.25-8-11.8z"/></symbol>
    <symbol id="i-flower" viewBox="0 0 24 24"><circle cx="12" cy="5.5" r="4"/><circle cx="17.6" cy="8.8" r="4"/><circle cx="17.6" cy="15.2" r="4"/><circle cx="12" cy="18.5" r="4"/><circle cx="6.4" cy="15.2" r="4"/><circle cx="6.4" cy="8.8" r="4"/><circle cx="12" cy="12" r="2.6" fill="var(--surface)"/></symbol>
    <symbol id="i-bloom" viewBox="0 0 24 24"><polygon points="12,1 22,18 2,18"/><polygon points="12,23 2,6 22,6"/><circle cx="12" cy="12" r="3" fill="var(--surface)"/></symbol>

    <symbol id="cycle-wheel" viewBox="0 0 360 440">
      <circle cx="176" cy="268" r="112" fill="none" stroke="var(--ring)" stroke-width="24"/>
      <path d="M67.3 240.9 A112 112 0 0 1 273 212" fill="none" stroke="var(--accent-light)" stroke-width="28" stroke-linecap="round"/>
      <path d="M121.7 170 A112 112 0 0 1 259.2 193.1" fill="none" stroke="var(--accent)" stroke-width="34" stroke-linecap="round"/>
      <path d="M139.5 374 A112 112 0 0 1 87.7 337" fill="none" stroke="var(--menses)" stroke-width="34" stroke-linecap="round"/>
      <use href="#i-flower" x="111" y="159" width="22" height="22" fill="#fff"/>
      <use href="#i-flower" x="60" y="234" width="14" height="14" fill="#fff"/>
      <use href="#i-drop" x="131" y="365" width="17" height="17" fill="#fff"/>
      <circle cx="176" cy="268" r="73" fill="var(--surface)" stroke="#e6e6e6" stroke-width="1.5"/>
      <use href="#i-drop" x="145" y="225" width="18" height="18" fill="var(--accent)"/>
      <text x="180" y="242" font-family="Roboto, sans-serif" font-size="24" fill="var(--ink)">17</text>
      <use href="#i-flower" x="146" y="262" width="16" height="16" fill="var(--accent)"/>
      <use href="#i-check" x="178" y="256" width="28" height="28" fill="var(--ink)"/>
      <use href="#i-bloom" x="143" y="296" width="22" height="22" fill="var(--accent)"/>
      <text x="186" y="315" font-family="Roboto, sans-serif" font-size="24" fill="var(--ink)">2</text>
      <circle cx="180" cy="87" r="29" fill="var(--accent)"/>
      <polygon points="156,104 204,104 180,128" fill="var(--accent)"/>
      <text x="180" y="97" text-anchor="middle" font-family="Roboto, sans-serif" font-weight="500" font-size="28" fill="#fff">14</text>
    </symbol>

    <symbol id="status-icons" viewBox="0 0 70 14">
      <path d="M0 2 Q8 -3 16 2 L8 12z" fill="#fff"/>
      <path d="M20 13 L33 1 L33 13z" fill="#fff" opacity=".6"/><path d="M20 13 L28 6 L28 13z" fill="#fff"/>
      <rect x="40" y="1" width="8" height="12" rx="1" fill="#fff" opacity=".6"/><rect x="40" y="7" width="8" height="6" fill="#fff"/>
    </symbol>
    <symbol id="nav-keys" viewBox="0 0 360 48">
      <path d="M86 24 L98 17 L98 31z" fill="none" stroke="#fff" stroke-width="2" stroke-linejoin="round"/>
      <circle cx="180" cy="24" r="7" fill="none" stroke="#fff" stroke-width="2"/>
      <rect x="272" y="17" width="14" height="14" rx="1" fill="none" stroke="#fff" stroke-width="2"/>
    </symbol>
  </defs>
</svg>

<main class="board">

  <section class="screen screen--top-left">
    <div class="status-bar"><svg class="status-bar__icons" width="50" height="14"><use href="#status-icons"/></svg><span class="status-bar__time">12:30</span></div>
    <header class="toolbar">
      <svg class="icon" style="left:16px"><use href="#i-menu"/></svg>
      <span class="toolbar__title">LunaTrak</span>
      <svg class="icon" style="left:176px"><use href="#i-list"/></svg>
      <svg class="icon" style="left:224px"><use href="#i-calendar"/></svg>
      <svg class="icon" style="left:272px"><use href="#i-chart"/></svg>
      <svg class="icon" style="left:320px"><use href="#i-hint"/></svg>
    </header>
    <svg class="wheel wheel--a"><use href="#cycle-wheel"/></svg>
    <div class="fab" style="top:520px"><svg class="icon"><use href="#i-edit"/></svg></div>
    <div class="nav-bar"><svg width="360" height="48"><use href="#nav-keys"/></svg></div>
  </section>

  <section class="screen screen--top-right">
    <div class="status-bar"><svg class="status-bar__icons" width="50" height="14"><use href="#status-icons"/></svg><span class="status-bar__time">12:30</span></div>
    <header class="toolbar">
      <svg class="icon" style="left:16px"><use href="#i-menu"/></svg>
      <span class="toolbar__title">LunaTrak</span>
      <svg class="icon" style="left:320px"><use href="#i-hint"/></svg>
    </header>
    <svg class="wheel wheel--b"><use href="#cycle-wheel"/></svg>
    <div class="fab" style="top:472px"><svg class="icon"><use href="#i-edit"/></svg></div>
    <nav class="action-bar">
      <div class="action-bar__item"><svg class="icon"><use href="#i-list"/></svg>Timeline</div>
      <div class="action-bar__item"><svg class="icon"><use href="#i-calendar"/></svg>Calendar</div>
      <div class="action-bar__item"><svg class="icon"><use href="#i-chart"/></svg>Charts</div>
    </nav>
    <div class="nav-bar"><svg width="360" height="48"><use href="#nav-keys"/></svg></div>
  </section>

  <section class="screen screen--bottom-left">
    <div class="status-bar"><svg class="status-bar__icons" width="50" height="14"><use href="#status-icons"/></svg><span class="status-bar__time">12:30</span></div>
    <header class="toolbar">
      <svg class="icon" style="left:16px"><use href="#i-menu"/></svg>
      <span class="toolbar__title">LunaTrak</span>
      <svg class="icon" style="left:320px"><use href="#i-hint"/></svg>
    </header>
    <svg class="wheel wheel--c"><use href="#cycle-wheel"/></svg>
    <nav class="mode-sheet">
      <span class="mode-sheet__title">View modes</span>
      <div class="mode-sheet__items">
        <div class="mode-sheet__item"><svg class="icon"><use href="#i-list"/></svg>Timeline</div>
        <div class="mode-sheet__item"><svg class="icon"><use href="#i-calendar"/></svg>Calendar</div>
        <div class="mode-sheet__item"><svg class="icon"><use href="#i-chart"/></svg>Charts</div>
      </div>
    </nav>
    <div class="fab" style="top:468px"><svg class="icon"><use href="#i-edit"/></svg></div>
    <div class="nav-bar"><svg width="360" height="48"><use href="#nav-keys"/></svg></div>
  </section>

  <section class="screen screen--bottom-right">
    <div class="status-bar"><svg class="status-bar__icons" width="50" height="14"><use href="#status-icons"/></svg><span class="status-bar__time">12:30</span></div>
    <header class="toolbar">
      <svg class="icon" style="left:16px"><use href="#i-menu"/></svg>
      <span class="toolbar__title">LunaTrak</span>
      <svg class="icon" style="left:320px"><use href="#i-hint"/></svg>
    </header>
    <svg class="wheel wheel--d"><use href="#cycle-wheel"/></svg>
    <ul class="mode-list">
      <li class="mode-list__item"><svg class="icon"><use href="#i-list"/></svg>Timeline</li>
      <li class="mode-list__item"><svg class="icon"><use href="#i-calendar"/></svg>Calendar</li>
      <li class="mode-list__item"><svg class="icon"><use href="#i-chart"/></svg>Charts</li>
    </ul>
    <div class="fab" style="top:444px"><svg class="icon"><use href="#i-edit"/></svg></div>
    <div class="nav-bar"><svg width="360" height="48"><use href="#nav-keys"/></svg></div>
  </section>

</main>
</body>
</html>
```